Startup photography business has a new logo, now we need business cards

Design a business card for the two partners of our business.
Our business Brisk Wombat has a new logo and we need to design a business card to showcase it and us.
Our colours of blue and orange are punchy and vivid, but how can we make the most of it on our card?

It should have our name Brisk Wombat
name of partner
phone number
email
website

Industry/Entity Type

Professional Photography

Contact Information for Business Card

Ewan Pottsworth
+61 455 81 76 93
ewan@briskwombat.com.au
briskwombat.com.au

second card
Liam Fairley
+61 419 628 315
liam@briskwombat.com.au
briskwombat.com.au

Colors
f37122
f68d4c
33a6d7
0592cd

Requirements
Must have
• one version of our logo, we have included options
• Name
• phone number
• email
• website
Nice to have
• instagram briskwombatstudio
• twitter briskwombatstudio
• facebook briskwombatstudio

```html
<!DOCTYPE html>
<html lang="en">
<head>
<meta charset="utf-8">
<title>Brisk Wombat — Business Cards</title>
<link rel="stylesheet" href="https://fonts.googleapis.com/css2?family=Russo+One&family=Roboto:wght@400;500&display=swap">
<style>
  :root {
    --stage: #e9e6e1;
    --card: #ffffff;
    --ink: #0d0d0d;
    --text: #2b2b2b;
    --orange: #f37122;
    --orange-soft: #f68d4c;
    --blue: #0592cd;
    --blue-soft: #33a6d7;
  }
  html, body {
    margin: 0;
    padding: 0;
    width: 1200px;
    height: 1023px;
    overflow: hidden;
    background: var(--stage);
  }
  .stage {
    width: 1200px;
    height: 1023px;
    display: flex;
    align-items: center;
    justify-content: center;
    gap: 80px;
  }
  .business-card {
    position: relative;
    width: 380px;
    height: 620px;
    background: var(--card);
    border-radius: 4px;
    box-shadow: 0 14px 40px rgba(0, 0, 0, 0.18);
    overflow: hidden;
  }
  .edge-band {
    position: absolute;
    left: 14px;
    right: 14px;
    height: 46px;
  }
  .edge-band--dark {
    top: 0;
    background: var(--ink);
    border-radius: 0 0 22px 22px;
  }
  .edge-band--accent {
    bottom: 0;
    background: var(--orange);
    border-radius: 22px 22px 0 0;
  }
  .brand {
    position: absolute;
    inset: 46px 0;
    display: flex;
    flex-direction: column;
    align-items: center;
    justify-content: center;
    gap: 24px;
  }
  .brand__mark {
    width: 110px;
    height: 110px;
  }
  .brand__name {
    margin: 0;
    font-family: "Russo One", sans-serif;
    font-weight: 400;
    font-size: 34px;
    letter-spacing: 1px;
    text-transform: uppercase;
    color: var(--orange);
    line-height: 1;
  }
  .contact {
    position: absolute;
    inset: 46px 0;
    padding: 0 40px;
    display: flex;
    flex-direction: column;
    justify-content: center;
  }
  .contact__name {
    margin: 0 0 6px;
    font-family: "Russo One", sans-serif;
    font-weight: 400;
    font-size: 30px;
    text-transform: uppercase;
    color: var(--orange);
    line-height: 1.1;
  }
  .contact__company {
    margin: 0 0 34px;
    font-family: "Russo One", sans-serif;
    font-size: 15px;
    letter-spacing: 2px;
    text-transform: uppercase;
    color: var(--blue);
  }
  .contact__list {
    list-style: none;
    margin: 0;
    padding: 0;
    display: flex;
    flex-direction: column;
    gap: 18px;
  }
  .contact__item {
    display: flex;
    align-items: center;
    gap: 14px;
    font-family: "Roboto", sans-serif;
    font-size: 16px;
    font-weight: 500;
    color: var(--text);
  }
  .contact__icon {
    flex: none;
    width: 30px;
    height: 30px;
    border-radius: 50%;
    background: var(--blue);
    display: flex;
    align-items: center;
    justify-content: center;
  }
  .contact__icon svg {
    width: 16px;
    height: 16px;
  }
</style>
</head>
<body>
  <main class="stage">
    <section class="business-card business-card--front" aria-label="Brisk Wombat business card front">
      <div class="edge-band edge-band--dark"></div>
      <div class="brand">
        <svg class="brand__mark" viewBox="0 0 110 110" aria-hidden="true">
          <circle cx="55" cy="55" r="48" fill="none" stroke="var(--orange)" stroke-width="9"/>
        </svg>
        <h1 class="brand__name">Brisk Wombat</h1>
      </div>
      <div class="edge-band edge-band--accent"></div>
    </section>

    <section class="business-card business-card--back" aria-label="Brisk Wombat business card back">
      <div class="edge-band edge-band--dark"></div>
      <div class="contact">
        <h2 class="contact__name">Ewan Pottsworth</h2>
        <p class="contact__company">Brisk Wombat</p>
        <ul class="contact__list">
          <li class="contact__item">
            <span class="contact__icon">
              <svg viewBox="0 0 16 16" aria-hidden="true"><path d="M4 1.5l2.5 3-1.5 1.5c.8 1.8 2.2 3.2 4 4l1.5-1.5 3 2.5-1.5 2.5C6.5 13.5 2.5 9.5 1.5 3z" fill="#fff"/></svg>
            </span>
            +61 455 81 76 93
          </li>
          <li class="contact__item">
            <span class="contact__icon">
              <svg viewBox="0 0 16 16" aria-hidden="true"><rect x="1.5" y="3.5" width="13" height="9" rx="1" fill="none" stroke="#fff" stroke-width="1.5"/><path d="M2 4l6 5 6-5" fill="none" stroke="#fff" stroke-width="1.5"/></svg>
            </span>
            ewan@briskwombat.com.au
          </li>
          <li class="contact__item">
            <span class="contact__icon">
              <svg viewBox="0 0 16 16" aria-hidden="true"><circle cx="8" cy="8" r="6" fill="none" stroke="#fff" stroke-width="1.5"/><path d="M2 8h12M8 2c2 2 2 10 0 12M8 2c-2 2-2 10 0 12" fill="none" stroke="#fff" stroke-width="1.2"/></svg>
            </span>
            briskwombat.com.au
          </li>
        </ul>
      </div>
      <div class="edge-band edge-band--accent"></div>
    </section>
  </main>
</body>
</html>
```